Invitation - Melbourne Show Invitation

We need an e-Invitation for our Trade Show in Melbourne. We are holding a furniture show at our Melbourne Showroom:

The Harbourline Private Show

Dates: Wednesday 19th to Friday 21st July

Hours: 9am to 6pm

Join us for Drinks on Thursday 20th from 5pm

Address:
The Lantern Loft
47 Arden Lane
Melbourne

RSVP: rosalind@harbourline-au.example

Tel. 03 9555 0172

The style of the building and the furniture is mid-century design, so I would like the invitation to reflect this (think "Tin Hats").

Target Market(s)

Professional Retailers

Industry/Entity Type

Trade

Font styles to use
Sans Serif

Colors

Designer to choose colors to be used in the design.

Requirements
Must have
• Dates and Times

```html
<!DOCTYPE html>
<html lang="en">
<head>
<meta charset="utf-8">
<title>The Harbourline Private Show – Melbourne Invitation</title>
<link rel="stylesheet" href="https://fonts.googleapis.com/css2?family=Lato:wght@300;400;900&display=swap">
<style>
  :root {
    --paper: #f3f1ec;
    --orange: #f07f2a;
    --ink: #231f20;
    --text-grey: #3a3a3a;
    --olive: #3d3b2c;
    --white: #ffffff;
  }
  html, body {
    margin: 0;
    padding: 0;
    overflow: hidden;
    background: var(--paper);
  }
  .invitation {
    position: relative;
    width: 1200px;
    height: 909px;
    overflow: hidden;
    background: var(--paper);
    font-family: "Lato", Arial, sans-serif;
    font-weight: 300;
    color: var(--text-grey);
  }
  .side-band {
    position: absolute;
    top: 0;
    right: 0;
    width: 84px;
    height: 909px;
    background: var(--orange);
  }

  /* Brand block */
  .brand-name {
    position: absolute;
    left: 112px;
    top: 205px;
    margin: 0;
    font-family: "Lato", Arial, sans-serif;
    font-weight: 900;
    color: var(--ink);
    line-height: 1;
  }
  .brand-name span { display: block; }
  .brand-name .line-the { font-size: 50px; margin-left: 50px; }
  .brand-name .line-main { font-size: 70px; letter-spacing: -2px; margin-top: 6px; }
  .brand-name .line-sub { font-size: 44px; margin-left: 78px; margin-top: 8px; }

  .furniture-art {
    position: absolute;
    left: 78px;
    top: 432px;
    width: 474px;
    height: 174px;
    border-radius: 18px;
    background: linear-gradient(180deg, #e6e3dc 0%, #d9d5cc 55%, #6b6854 100%);
  }
  .city-bar {
    position: absolute;
    left: 94px;
    top: 627px;
    width: 443px;
    height: 60px;
    background: var(--orange);
    border-bottom: 5px solid var(--olive);
    box-shadow: 0 3px 0 var(--paper);
    color: var(--white);
    font-size: 31px;
    font-weight: 300;
    text-align: center;
    line-height: 60px;
  }

  .divider {
    position: absolute;
    left: 598px;
    top: 203px;
    width: 2px;
    height: 504px;
    background: var(--orange);
  }

  /* Details */
  .details {
    position: absolute;
    right: 123px;
    top: 148px;
    width: 420px;
    text-align: right;
  }
  .details p { margin: 0; }
  .invite-line { font-size: 21px; line-height: 30px; }
  .event-title { font-size: 34px; line-height: 46px; margin-top: 2px !important; }
  .rule {
    height: 2px;
    background: var(--orange);
    margin: 0;
    border: 0;
  }
  .rule.top { margin-top: 10px; }
  .date-block { color: var(--orange); font-weight: 400; padding: 12px 0 10px; }
  .weekday { font-size: 32px; line-height: 38px; }
  .dates { font-size: 64px; line-height: 72px; white-space: nowrap; }
  .dates sup { font-size: 34px; vertical-align: 26px; line-height: 0; }
  .dates .to { font-size: 30px; }
  .hours { font-size: 31px; line-height: 40px; margin-right: 16px !important; }
  .drinks { font-size: 32px; line-height: 44px; margin-top: 16px !important; }
  .drinks sup { font-size: 17px; vertical-align: 14px; line-height: 0; }
  .address-label {
    font-size: 25px;
    line-height: 32px;
    color: var(--orange);
    font-weight: 400;
    text-decoration: underline;
    text-underline-offset: 3px;
    margin-top: 10px !important;
  }
  .address { font-style: normal; font-size: 25px; line-height: 33px; }
  .contact { font-size: 25px; line-height: 34px; margin-top: 12px !important; }
  .contact a { color: inherit; text-decoration: none; }
</style>
</head>
<body>
<main class="invitation">
  <div class="side-band"></div>

  <h1 class="brand-name">
    <span class="line-the">The</span>
    <span class="line-main">Harbourline</span>
    <span class="line-sub">Private Show</span>
  </h1>

  <div class="furniture-art" role="img" aria-label="Illustration of a mid-century armchair and sofa with orange cushions"></div>

  <div class="city-bar">Melbourne</div>

  <div class="divider"></div>

  <section class="details">
    <p class="invite-line">You are cordially invited to</p>
    <p class="event-title">The Harbourline Private Show</p>
    <hr class="rule top">
    <div class="date-block">
      <p class="weekday">Wednesday</p>
      <p class="dates">19<sup>th</sup> <span class="to">to</span> 21<sup>st</sup> July</p>
      <p class="hours">9am to 6pm</p>
    </div>
    <hr class="rule">
    <p class="drinks">Join us for Drinks on<br>Thursday 20<sup>th</sup> from 5pm</p>
    <p class="address-label">Address</p>
    <address class="address">The Lantern Loft<br>47 Arden Lane<br>Melbourne</address>
    <p class="contact">RSVP: <a href="mailto:rosalind@harbourline-au.example">rosalind@harbourline-au.example</a><br>Tel. 03 9555 0172</p>
  </section>
</main>
</body>
</html>
```